Family Entertainment Center needs a fundraising flyer design

We need a 8.5 x 5.5 (half sheet of copy paper) flyer designed for a roller skating rink/family entertainment center in Wichita, KS. We partner with 100s of local schools each year by offering PTO fundraisers at our facility. With each party we send out flyers to the schools to send home with each kid to remind them of the time and date of the party as well as get them excited! Most of these schools and PTOs call these fundraisers "skate night".The information we need communicated or on our flyer is below:-Skating $6-Play Zone $6-Skate & Play $10-Skate Rental is included in above pricing-Price is per person-www.maplewheelrink.com-Maplewood Skate Center 847 S. Pinecrest Ave. Wichita, KS 67219-Our logo (attached)-The words or heading "Skate Night"-A blank, white space for us to print details in (see attached flyer for an example)

Target Market(s)

Elementary School parents and kids

Font styles to use
Serif
Sans Serif

Requirements
Must have
• The information outlined in the description and a blank white space incorporated into the design for our ability to print over.
Nice to have
• colors that match or compliment our logo, creative, but clean fonts

```html
<!DOCTYPE html>
<html lang="en">
<head>
<meta charset="utf-8">
<title>Skate Night Flyer – Maplewood Skate Center</title>
<link href="https://fonts.googleapis.com/css2?family=Montserrat:wght@500;600;700;800&display=swap" rel="stylesheet">
<style>
  :root {
    --wall-dark: #141a3f;
    --wall-mid: #262f6b;
    --wall-glow: #3a3f8a;
    --neon-yellow: #ffd23a;
    --neon-gold: #f6b21f;
    --neon-pink: #f24bd0;
    --neon-purple: #8b4ee0;
    --price-pink: #ff5ad6;
    --fine-red: #ff3b3b;
    --white: #ffffff;
    --photo-border: #f7f7f7;
    --string: #1b1b1b;
  }
  * { margin: 0; padding: 0; box-sizing: border-box; }
  html, body { width: 776px; height: 1200px; overflow: hidden; }
  body { font-family: "Montserrat", Arial, sans-serif; background: var(--wall-dark); }

  .flyer {
    position: relative;
    width: 776px; height: 1200px; overflow: hidden;
    background:
      radial-gradient(ellipse 70% 45% at 50% 40%, var(--wall-glow) 0%, transparent 70%),
      linear-gradient(180deg, var(--wall-mid) 0%, var(--wall-dark) 100%);
  }

  /* hanging photos */
  .photo-line { position: absolute; top: 0; width: 2px; background: var(--string); }
  .photo-clip { position: absolute; width: 14px; height: 10px; background: #2a2a2a; border-radius: 2px; }
  .photo {
    position: absolute;
    border: 8px solid var(--photo-border);
    box-shadow: 0 6px 14px rgba(0,0,0,.45);
  }
  .photo--a { left: 47px; top: 110px; width: 106px; height: 145px; background: linear-gradient(160deg,#5a3a8a,#c94fa8 60%,#3b2a5e); }
  .photo--b { left: 167px; top: 59px; width: 104px; height: 102px; background: linear-gradient(160deg,#4a6ea8,#d9c7c2 55%,#6b4f8f); }
  .photo--c { left: 286px; top: 169px; width: 141px; height: 98px; background: linear-gradient(160deg,#3d4d3a,#a36a4a 55%,#2c2c3e); }
  .photo--d { left: 453px; top: 59px; width: 102px; height: 145px; background: linear-gradient(160deg,#2c2e5a,#c8a08a 50%,#3b5a4a); }
  .photo--e { left: 582px; top: 125px; width: 143px; height: 100px; background: linear-gradient(160deg,#1e2f6a,#3c88c8 50%,#c0623a); }

  /* title */
  .skate-icon {
    position: absolute; left: 86px; top: 304px; width: 192px; height: 210px;
    background: radial-gradient(ellipse at 45% 50%, rgba(242,75,208,.55) 0%, rgba(139,78,224,.35) 45%, transparent 72%);
  }
  .title-skate, .title-night {
    position: absolute; font-weight: 700; letter-spacing: 4px; line-height: 1;
  }
  .title-skate {
    left: 288px; top: 306px; font-size: 112px;
    color: transparent;
    -webkit-text-stroke: 5px var(--neon-yellow);
    text-shadow: 0 0 14px rgba(255,196,40,.75);
  }
  .title-night {
    left: 306px; top: 412px; font-size: 104px; color: var(--white);
    text-shadow: 0 0 12px rgba(255,255,255,.45);
  }

  .tagline {
    position: absolute; left: 84px; top: 518px; width: 606px; height: 51px;
    border: 4px solid var(--neon-purple); border-radius: 4px;
    box-shadow: 0 0 10px rgba(139,78,224,.8);
    display: flex; align-items: center; justify-content: center;
    color: var(--neon-yellow); font-weight: 800; font-size: 29px; letter-spacing: 1px;
  }

  /* marquee print area */
  .marquee { position: absolute; left: 70px; top: 598px; width: 636px; height: 323px; }
  .print-area {
    position: absolute; left: 98px; top: 625px; width: 580px; height: 270px;
    background: var(--white); border-radius: 10px;
  }

  .promo {
    position: absolute; left: 202px; top: 946px; width: 512px; height: 44px;
    border: 4px solid var(--neon-purple); border-radius: 6px;
    box-shadow: 0 0 10px rgba(139,78,224,.7);
    display: flex; align-items: center; justify-content: center;
    color: var(--price-pink); font-weight: 700; font-size: 25px;
  }

  /* pricing */
  .prices {
    position: absolute; left: 172px; top: 1004px; width: 570px;
    display: flex; align-items: center; justify-content: space-between;
  }
  .price { display: flex; align-items: center; gap: 6px; color: var(--white); }
  .price__amount { color: var(--neon-yellow); font-weight: 800; font-size: 40px; line-height: 1; }
  .price__amount sup { font-size: 20px; vertical-align: 16px; }
  .price__label { font-weight: 700; font-size: 18px; line-height: 1.05; }
  .price__divider { width: 3px; height: 44px; background: var(--white); }

  .fine-print {
    position: absolute; left: 172px; top: 1062px; width: 570px; text-align: center;
    color: var(--fine-red); font-size: 14.5px; font-weight: 600;
  }
  .venue {
    position: absolute; left: 172px; top: 1084px; width: 570px; text-align: center;
    color: var(--white); line-height: 1.15;
  }
  .venue__name { font-weight: 600; font-size: 20px; }
  .venue__address { font-weight: 500; font-size: 19px; }

  .website {
    position: absolute; left: 294px; top: 1146px; width: 388px; height: 37px;
    border: 3px solid var(--neon-purple); border-radius: 4px;
    display: flex; align-items: center; justify-content: center;
    color: var(--price-pink); font-weight: 700; font-size: 21px;
  }

  /* brand */
  .brand {
    position: absolute; left: 14px; top: 1040px; width: 150px;
    display: flex; flex-direction: column; align-items: center; gap: 8px;
  }
  .brand__mark { width: 56px; height: 56px; border-radius: 50%; background: var(--white); }
  .brand__name {
    color: var(--white); font-weight: 800; font-size: 18px; line-height: 1.1; text-align: center; letter-spacing: 1px;
  }
</style>
</head>
<body>
<div class="flyer">

  <!-- hanging photos -->
  <div class="photo-line" style="left:99px;height:110px"></div>
  <div class="photo-line" style="left:218px;height:59px"></div>
  <div class="photo-line" style="left:356px;height:169px"></div>
  <div class="photo-line" style="left:503px;height:59px"></div>
  <div class="photo-line" style="left:653px;height:125px"></div>
  <div class="photo photo--a" role="img" aria-label="Photo of a child roller skating"></div>
  <div class="photo photo--b" role="img" aria-label="Photo of a group of kids on skates"></div>
  <div class="photo photo--c" role="img" aria-label="Photo of a school group at the rink"></div>
  <div class="photo photo--d" role="img" aria-label="Photo of a smiling child in the play zone"></div>
  <div class="photo photo--e" role="img" aria-label="Photo of kids playing in the play zone"></div>
  <div class="photo-clip" style="left:93px;top:104px"></div>
  <div class="photo-clip" style="left:212px;top:53px"></div>
  <div class="photo-clip" style="left:350px;top:163px"></div>
  <div class="photo-clip" style="left:497px;top:53px"></div>
  <div class="photo-clip" style="left:647px;top:119px"></div>

  <!-- title -->
  <div class="skate-icon" role="img" aria-label="Neon pink roller skate illustration"></div>
  <div class="title-skate">SKATE</div>
  <div class="title-night">NIGHT</div>
  <div class="tagline">FAMILY-FUN ENTERTAINMENT</div>

  <!-- marquee frame -->
  <svg class="marquee" viewBox="0 0 636 323" aria-hidden="true">
    <defs>
      <linearGradient id="frameGold" x1="0" y1="0" x2="0" y2="1">
        <stop offset="0" stop-color="#ffcf4a"/>
        <stop offset="1" stop-color="#e79a12"/>
      </linearGradient>
      <radialGradient id="bulb">
        <stop offset="0" stop-color="#fffbe6"/>
        <stop offset="0.6" stop-color="#ffe58a"/>
        <stop offset="1" stop-color="#f6b21f"/>
      </radialGradient>
    </defs>
    <rect x="2" y="2" width="632" height="319" rx="22" fill="url(#frameGold)" stroke="#fff3c0" stroke-width="3" style="filter:drop-shadow(0 0 10px rgba(255,190,40,.8))"/>
    <g fill="url(#bulb)">
      <circle cx="50" cy="14" r="6"/><circle cx="110" cy="14" r="6"/><circle cx="170" cy="14" r="6"/><circle cx="230" cy="14" r="6"/><circle cx="290" cy="14" r="6"/><circle cx="350" cy="14" r="6"/><circle cx="410" cy="14" r="6"/><circle cx="470" cy="14" r="6"/><circle cx="530" cy="14" r="6"/><circle cx="590" cy="14" r="6"/>
      <circle cx="50" cy="309" r="6"/><circle cx="110" cy="309" r="6"/><circle cx="170" cy="309" r="6"/><circle cx="230" cy="309" r="6"/><circle cx="290" cy="309" r="6"/><circle cx="350" cy="309" r="6"/><circle cx="410" cy="309" r="6"/><circle cx="470" cy="309" r="6"/><circle cx="530" cy="309" r="6"/><circle cx="590" cy="309" r="6"/>
      <circle cx="14" cy="50" r="6"/><circle cx="14" cy="105" r="6"/><circle cx="14" cy="160" r="6"/><circle cx="14" cy="215" r="6"/><circle cx="14" cy="270" r="6"/>
      <circle cx="622" cy="50" r="6"/><circle cx="622" cy="105" r="6"/><circle cx="622" cy="160" r="6"/><circle cx="622" cy="215" r="6"/><circle cx="622" cy="270" r="6"/>
    </g>
  </svg>
  <div class="print-area"></div>

  <div class="promo">Don’t miss our new Play Zone !</div>

  <!-- pricing -->
  <div class="prices">
    <div class="price"><span class="price__amount"><sup>$</sup>6</span><span class="price__label">Skating</span></div>
    <div class="price__divider"></div>
    <div class="price"><span class="price__amount"><sup>$</sup>6</span><span class="price__label">Play<br>Zone</span></div>
    <div class="price__divider"></div>
    <div class="price"><span class="price__amount"><sup>$</sup>10</span><span class="price__label">Skate &amp;<br>Play</span></div>
    <div class="price__divider"></div>
    <div class="price"><span class="price__amount"><sup>$</sup>13</span><span class="price__label">Ultimate<br>Pass</span></div>
  </div>

  <p class="fine-print">Skate Rental is included in above pricing-Price is per person</p>
  <div class="venue">
    <p class="venue__name">Maplewood Skate Center</p>
    <p class="venue__address">847 S. Pinecrest Ave. Wichita, KS 67219</p>
  </div>
  <div class="website">www.maplewheelrink.com</div>

  <div class="brand">
    <div class="brand__mark"></div>
    <p class="brand__name">MAPLEWOOD<br>SKATE</p>
  </div>

</div>
</body>
</html>
```